Business Card Design For A Cajun Seafood Restaurant

We are opening a cajun seafood restaurant in a week. We mainly serve cajun seafood which is orginally from Louisiana. We want design on both sides of a business card. I have menu on the website. You can go to www.bayourelish.com to check out our menu.

Restaurant name: Bayou Relish
Phone: +1 (818) 555-4172
Address: 48627 Dellmont Row, #5, Fernhollow, Ca90847
Email: bayourelish@mailbox.example
Website: www.bayourelish.com

Maybe add social media icons (facebook, instagram) if looks nice on the business card.
facebook.com/bayourelish
instagram.com/bayourelish or @bayourelish

Attached is the logo and other business card samples that I like.

```html
<!DOCTYPE html>
<html lang="en">
<head>
<meta charset="utf-8">
<title>Bayou Relish — Business Card</title>
<link href="https://fonts.googleapis.com/css2?family=Open+Sans:wght@400;600;700&display=swap" rel="stylesheet">
<style>
  :root {
    --page: #e9e6e1;
    --card-light: #d9d7d2;
    --card-dark: #262423;
    --ink: #3a3836;
    --accent: #e8622a;
    --accent-deep: #c94a1a;
    --light-text: #cfcac4;
  }
  * { box-sizing: border-box; margin: 0; padding: 0; }
  html, body { width: 1200px; height: 848px; overflow: hidden; }
  body {
    background: var(--page);
    font-family: "Open Sans", sans-serif;
    display: flex;
    align-items: center;
    justify-content: center;
    gap: 48px;
  }
  .card {
    position: relative;
    width: 540px;
    height: 309px;
    border-radius: 22px;
    box-shadow: 0 10px 28px rgba(0,0,0,0.18);
    overflow: hidden;
  }
  .card--front { background: var(--card-light); }
  .card--back { background: var(--card-dark); }

  .brand {
    position: absolute;
    display: flex;
    flex-direction: column;
    align-items: center;
  }
  .brand__art {
    border-radius: 50%;
    background: radial-gradient(circle at 45% 40%, #f08a3c, var(--accent-deep));
  }
  .brand__name {
    margin-top: 10px;
    font-weight: 600;
    white-space: nowrap;
  }
  .card--front .brand { left: 40px; top: 118px; width: 220px; }
  .card--front .brand__art { width: 96px; height: 84px; }
  .card--front .brand__name { font-size: 22px; color: var(--ink); }

  .card--back .brand { left: 0; right: 0; top: 38px; }
  .card--back .brand__art { width: 128px; height: 110px; }
  .card--back .brand__name { font-size: 28px; color: var(--light-text); }

  .contact {
    position: absolute;
    left: 290px;
    top: 48px;
    color: var(--ink);
  }
  .contact__name { font-size: 20px; font-weight: 600; line-height: 1.1; }
  .contact__title { font-size: 11px; color: var(--accent); margin-bottom: 18px; }
  .contact__list { list-style: none; font-size: 11.5px; line-height: 1.5; }
  .contact__list li { display: flex; gap: 8px; margin-bottom: 4px; }
  .contact__list svg { flex: none; width: 12px; height: 12px; margin-top: 3px; }

  .social {
    position: absolute;
    left: 40px;
    right: 30px;
    bottom: 30px;
    display: flex;
    justify-content: space-between;
    list-style: none;
    color: var(--light-text);
    font-size: 14px;
  }
  .social li { display: flex; align-items: center; gap: 8px; }
  .social__mark { width: 12px; height: 12px; background: var(--accent); border-radius: 2px; }
</style>
</head>
<body>
  <section class="card card--front">
    <div class="brand">
      <div class="brand__art" role="img" aria-label="Cartoon crab mascot illustration holding an ear of corn"></div>
      <div class="brand__name">Bayou Relish</div>
    </div>
    <div class="contact">
      <p class="contact__name">Your Name</p>
      <p class="contact__title">Job Title</p>
      <ul class="contact__list">
        <li>
          <svg viewBox="0 0 12 12"><path fill="var(--accent)" d="M2.5 1h2l1 3-1.3 1a6 6 0 0 0 2.8 2.8l1-1.3 3 1v2a1 1 0 0 1-1 1A9.5 9.5 0 0 1 1.5 2a1 1 0 0 1 1-1z"/></svg>
          +1 (818) 555-4172
        </li>
        <li>
          <svg viewBox="0 0 12 12"><path fill="var(--accent)" d="M6 0.5a4 4 0 0 1 4 4c0 3-4 7-4 7s-4-4-4-7a4 4 0 0 1 4-4zm0 2.3a1.7 1.7 0 1 0 0 3.4 1.7 1.7 0 0 0 0-3.4z"/></svg>
          <span>48627 Dellmont Row<br>#5, Fernhollow, Ca90847</span>
        </li>
        <li>
          <svg viewBox="0 0 12 12"><rect x="0.5" y="2" width="11" height="8" rx="1" fill="var(--accent)"/><path d="M1 2.8l5 3.6 5-3.6" stroke="var(--card-light)" stroke-width="1" fill="none"/></svg>
          bayourelish@mailbox.example
        </li>
        <li>
          <svg viewBox="0 0 12 12" fill="none" stroke="var(--accent)" stroke-width="1"><circle cx="6" cy="6" r="5"/><ellipse cx="6" cy="6" rx="2.2" ry="5"/><path d="M1 6h10M2 3.5h8M2 8.5h8"/></svg>
          www.bayourelish.com
        </li>
      </ul>
    </div>
  </section>

  <section class="card card--back">
    <div class="brand">
      <div class="brand__art" role="img" aria-label="Cartoon crab mascot illustration holding an ear of corn"></div>
      <div class="brand__name">Bayou Relish</div>
    </div>
    <ul class="social">
      <li><span class="social__mark"></span>facebook.com/bayourelish</li>
      <li><span class="social__mark"></span>instagram.com/bayourelish</li>
    </ul>
  </section>
</body>
</html>
```